IT Company needs full suite of stationery

Our company 4627 Vantrel Works Ltd. is an IT company based in Toronto, Canada. Based on our logo we would like to see business cards(front and back), letterhead, envelope, brochure template. Design would be simple, not too bright, modern but can be used for many years, good theme throughout. Our official logo is the the fullcolor_a, full company name is 4627 Vantrel Works Ltd., Please include full company name on all pieces. Logo can be modified to be the graphic only with the "4627 Works", I have cropped it myself for a couple files but I am no designer. We will provide lots of feedback so post early and often.
Updates

Project Deadline Extended
Reason: Very busy around the holidays, like a lot of the designs currently submitted, will definitely be picking one. Thanks for your submissions and merry Christmas and Happy New Year to everyone.

Industry/Entity Type

Business

```html
<!DOCTYPE html>
<html lang="en">
<head>
<meta charset="utf-8">
<title>4627 Vantrel Works Ltd. – Business Card</title>
<link rel="stylesheet" href="https://fonts.googleapis.com/css2?family=Lato:wght@300;400;700&display=swap">
<style>
  :root {
    --backdrop: #2b2b2c;
    --card-white: #f4f4f4;
    --card-dark: #3e3c3b;
    --card-dark-deep: #2c2a29;
    --ink: #231f20;
    --ink-soft: #3a3a3a;
    --brand-green: #3fb27a;
    --brand-green-deep: #2e9a5f;
    --band-light: #d9d9d9;
    --band-dark: #1c1c1c;
  }
  * { box-sizing: border-box; margin: 0; padding: 0; }
  html, body {
    width: 1200px; height: 1000px; overflow: hidden;
    background: var(--backdrop);
    font-family: "Lato", Arial, sans-serif;
  }
  .sheet {
    position: relative; width: 1200px; height: 1000px;
  }
  .card {
    position: absolute; top: 150px; width: 400px; height: 700px;
    box-shadow: 0 10px 30px rgba(0,0,0,.45);
  }
  /* ---------- front ---------- */
  .card-front {
    left: 150px;
    background: var(--card-white);
    padding: 14px;
  }
  .front-field {
    position: relative; width: 100%; height: 100%;
    background: linear-gradient(180deg, var(--card-dark) 0%, var(--card-dark-deep) 100%);
    overflow: hidden;
  }
  .front-mark {
    position: absolute; top: 70px; left: 50%; transform: translateX(-50%);
    width: 64px; height: 64px; border-radius: 50%;
    background: var(--card-white);
  }
  .front-band {
    position: absolute; top: 230px; left: 0; width: 100%; height: 190px;
    background: linear-gradient(180deg, var(--band-dark) 0%, #5a5a5a 45%, var(--band-light) 55%, #4a4a4a 70%, var(--band-dark) 100%);
  }
  .front-namebox {
    position: absolute; top: 270px; left: 110px; width: 240px; height: 90px;
    background: rgba(240,240,240,.92);
    display: flex; align-items: center; justify-content: flex-end; padding-right: 22px;
  }
  .front-name {
    font-size: 30px; font-weight: 700; color: var(--ink-soft); letter-spacing: 1px;
  }
  .front-tag {
    position: absolute; top: 345px; left: 40px; width: 190px; height: 42px;
    background: var(--brand-green);
    color: #fff; font-size: 15px; font-weight: 400; letter-spacing: 1px;
    display: flex; align-items: center; padding-left: 20px;
  }
  /* ---------- back ---------- */
  .card-back {
    left: 650px;
    background: linear-gradient(180deg, #f7f7f7 0%, #e6e6e6 100%);
  }
  .back-mark {
    position: absolute; top: 60px; left: 50%; transform: translateX(-50%);
    width: 76px; height: 76px; border-radius: 50%;
    background: var(--brand-green-deep);
  }
  .back-namebar {
    position: absolute; top: 190px; left: 50px; width: 300px; height: 78px;
    background: var(--ink);
    display: flex; align-items: center; justify-content: center;
  }
  .back-name {
    color: #f2f2f2; font-size: 32px; font-weight: 700; letter-spacing: 1px;
  }
  .back-person {
    position: absolute; top: 390px; left: 70px;
  }
  .person-name {
    color: var(--brand-green); font-size: 28px; font-weight: 300; letter-spacing: 2px;
  }
  .person-title {
    color: var(--ink-soft); font-size: 20px; font-weight: 400; margin-top: 4px;
  }
  .back-contact {
    position: absolute; top: 500px; left: 90px;
    list-style: none; color: var(--ink-soft); font-size: 15px; line-height: 30px;
  }
</style>
</head>
<body>
<main class="sheet">
  <section class="card card-front" aria-label="Business card front">
    <div class="front-field">
      <div class="front-mark"></div>
      <div class="front-band" role="img" aria-label="Monochrome technology scene with streams of binary digits and computer screens"></div>
      <div class="front-namebox"><span class="front-name">4627 Works</span></div>
      <div class="front-tag">LOREM IPSUM</div>
    </div>
  </section>

  <section class="card card-back" aria-label="Business card back">
    <div class="back-mark"></div>
    <div class="back-namebar"><span class="back-name">4627 Works</span></div>
    <div class="back-person">
      <p class="person-name">LOREM IPSUM</p>
      <p class="person-title">Title</p>
    </div>
    <ul class="back-contact">
      <li>+ 00 0000 0000 00</li>
      <li>companyname@domain.com</li>
      <li>www.companyname.com</li>
    </ul>
  </section>
</main>
</body>
</html>
```